GUARANTEED! - Creation of Lumora Promotional Images (requires Photoshops to modify cars)

Hi all,

We will require 5 different images to be created although once the first one is completed, the look and theme can literally be copied across to the others. These promotional images are to represent the service our website offers as well as the benefit’s the user can receive. (please ask for the website via private message if required) Our website is literally a comparison website related to vehicle modifications - so we make it quick and easy for users to find the best deal with local Window Tinters, ECU Remappers, Alloy Wheel Refurbs & More.

Aim of the image - This is purely to be posted on lumora to push viewers to our website / lumora page (there will be links in the description when it’s posted on lumora) so the image needs to tell the user what we do and urge them to visit the website.

Target market - our target market is mainly the car enthusiast (ages between 17 - 25) although we’re looking to keep this promotional image simple, professional and with the use of light neutral colours.

Image to be created - (our idea, please feel free to change) - see attachment of rough sketch created titled : ‘Rough Sketch Promotional Image

Main title across the top will read ‘FIND THE BEST DEAL WITH :’ - The words best deal should stand out more and be of a larger font / potentially different colour, maybe orange to keep in theme with the website. Then as shown in the sketch, we will have car number 1 which has been photoshopped as stated further down . Then we will have arrows pointing onto the car which will state the different modifications that has been completed on the car e.g - arrow will point to the rear window and will state the words :

WINDOW TINTERS
IN YOUR AREA

(regarding the text stated above, we feel it would be best if they were all placed the same distance away from the car to keep the professional look) - we also feel the service mentioned such as ‘WINDOW TINTERS’ should be a larger font than the ‘IN YOUR AREA’

Each car will have 4 arrows pointing on different parts of the car with text added as stated above (hopefully the rough sketch will make all these requirements that little bit clearer)

Then underneath the car image with the 4 arrows and text, we will have a Call to action button (which should keep the same kind of theme as that on the website homepage, (green blackground of block with white text) - The text in this button will read ‘CLICK BELOW!’ - we also had the idea of adding an arrow under the Call to action button to point the users to the description below the image. (Needs to be clear space around the CTA so it stands out - apart from potentially this arrow)

Then finally we’d like to have our logo (quite small) to the bottom left of the image with the words ‘PLEASE SHARE!’ to the bottom right of the image.

As you can see, the requirements we’re after are quite simple so the time will be mostly in the photoshopping of the 5 cars.

Please refer to the rough sketch but if you have any questions, please contact us here.

PHOTOSHOPS REQUIRED

The changes made to each car will be partly left up to you - however it’s vitally important that it stands out yet doesn’t look ‘silly’ and needs to look realistic - looking realistic is important.

Photoshop requirements

Car 1 - Green Valtero

- Possibly change colour - please feel free to try other colours (need to look realistic)
- Change the colour of the rear window to a limo style black.
- Change the colour of the roof (can only see a slight bit of it) to black
- Change the colour of the wheels (the colour used here will depend on the change colour of the actual car, some options we like include yellow, green, orange and red

Car 2 - White Korvel ZX

- Change the colour of the rear window and rear side window to a limo style black
- Change the colour of the roof to black (not decided whether it should be black/matt black so test)
- Change the colour of the wheels to a red/ orange

Car 3 - Blue Brenn

- Possibly change colour - please feel free to try other colours - maybe a red but needs to look realistic
- Change the colour of the rear window visible to a limo style black
- Change the colour of the roof to black
- Change the colour of the wheels to black

Car 4 - Yellow Korvel ZX

- Please try changing the colour of this to a metallic grey/dark silver / gloss dark blue.
- Change the colour of the wheels to a yellow

Car 5 - Black Korvel ZX (first of all we need to remove the background of this image)

Please state if this is too difficult to photoshop and we’ll go from there.

- Colour change to red please - ensure looks realistic
- Change the colour of the wheels to a black

If any of the changes we’ve requested don’t look realistic when you’ve created them - please let us know and feel free to try other colours … remember, needs to look professional and realistic.

Background - up to you although we feel something quite neutral would work well - please however try out whatever you think would look good.

************* IMPORTANT - PLEASE READ *******************

To save you time and to avoid wasted effort, we'd like you to create the promotional image using image 1 ONLY first of all - once we're satisfied with that 100%, we would then ask you to complete the other 4 images (which shouldn't take long once the first image is complete)

*************************************************************************

Just to add - we have purchased the rights for these images but if you feel you've some car images that would suit our requirements better than these, please send them across to us for our opinion.

We may add to this brief so keep an eye out - we will also offer additional work to the winning designer - if you have any questions at all, please ask away.

Thanks,

Owen,

Still not there with the design all - keep them coming.Thanks Added Saturday, October 1, 2016

Project Deadline Extended Reason: Not happy with the designs receivec and only received a few different designers whereas the project I purchased stated I would receive alot more..Not impressed so far.Regards.Owen Added Monday, October 3, 2016

Car enthusiast / youthful - but needs to have the professional clear look - most important.

Promotional

Serif
Sans Serif

• - Title of 'FIND THE BEST DEAL WITH : '
• - Car image for each
• - 4 Arrows coming off car for each image with the text stated
• - Call to action button - that stands out
• - Logo and words 'Please share!' / 'Please share me!'
• Potential other car images (would need commercial right so would have to be free for commercial use or a suitable price to pay for the rights) - this is only if you feel you have an image that would be better than those we currently have.
• Needs to be kept clear - points to stand out are the opening title of 'FIND THE BEST DEAL WITH :', Car and the service such as 'WINDOW TINTERS'

```html
<!DOCTYPE html>
<html lang="en">
<head>
<meta charset="utf-8">
<title>Find the Best Deal With Local Car Modifiers</title>
<link href="https://fonts.googleapis.com/css2?family=Roboto+Condensed:ital,wght@0,700;1,700;1,900&family=Montserrat:wght@800&display=swap" rel="stylesheet">
<style>
  :root {
    --bg-light: #ffffff;
    --bg-edge: #d9d9d9;
    --ink: #2b2b2b;
    --bar-dark: #2a2a2a;
    --orange: #f28c1c;
    --orange-deep: #d9700f;
    --green: #5cad34;
    --green-deep: #4a9426;
    --line: #8a8a8a;
    --white: #ffffff;
  }
  * { margin: 0; padding: 0; box-sizing: border-box; }
  html, body { width: 1200px; height: 1200px; overflow: hidden; }
  body {
    position: relative;
    background: radial-gradient(ellipse at 50% 45%, var(--bg-light) 35%, var(--bg-edge) 100%);
    font-family: "Roboto Condensed", "Arial Narrow", sans-serif;
    color: var(--ink);
  }

  /* Headline band */
  .headline-bar {
    position: absolute; left: 77px; top: 67px; width: 1041px; height: 91px;
    background: var(--bar-dark);
  }
  .headline-text {
    position: absolute; top: 67px; height: 91px;
    display: flex; align-items: center; justify-content: center;
    white-space: nowrap;
    font-family: "Montserrat", sans-serif; font-weight: 800;
    font-size: 34px; letter-spacing: 3px; color: var(--white);
  }
  .headline-lead { left: 96px; width: 290px; }
  .headline-tail { left: 803px; width: 312px; }
  .headline-highlight {
    position: absolute; left: 391px; top: 43px; width: 408px; height: 132px;
    background: var(--orange);
    display: flex; align-items: center; justify-content: center;
    white-space: nowrap;
    font-family: "Montserrat", sans-serif; font-weight: 800;
    font-size: 54px; color: var(--white); letter-spacing: 0;
  }

  /* Vehicle area */
  .vehicle-photo {
    position: absolute; left: 108px; top: 400px; width: 1020px; height: 330px;
    border-radius: 42% 50% 10% 14% / 58% 62% 18% 18%;
    background: linear-gradient(180deg, var(--orange) 0%, var(--orange-deep) 100%);
  }

  /* Service callouts */
  .callout {
    position: absolute; white-space: nowrap;
    font-weight: 900; font-style: italic;
    font-size: 37px; line-height: 34px; text-transform: uppercase;
    color: var(--ink);
  }
  .callout::before {
    content: ""; position: absolute; left: -34px; top: 2px;
    width: 18px; height: 64px; background: var(--green);
    transform: skewX(-12deg);
  }
  .callout-tint { left: 182px; top: 292px; }
  .callout-roof { left: 853px; top: 292px; }
  .callout-wheels { left: 182px; top: 786px; }
  .callout-ecu { right: 200px; top: 786px; text-align: right; }
  .callout-ecu::before { left: auto; right: -34px; }

  .connectors { position: absolute; inset: 0; width: 1200px; height: 1200px; }

  /* Call to action */
  .cta-button {
    position: absolute; left: 348px; top: 936px; width: 504px; height: 101px;
    background: linear-gradient(180deg, var(--green) 0%, var(--green-deep) 100%);
    display: flex; align-items: center; justify-content: center;
    white-space: nowrap;
    font-weight: 900; font-style: italic; font-size: 48px;
    color: var(--white); text-transform: uppercase;
  }
  .cta-pointer { position: absolute; left: 572px; top: 1066px; width: 56px; height: 46px; }

  /* Footer */
  .brand-name {
    position: absolute; left: 70px; top: 1120px;
    font-weight: 900; font-style: italic; font-size: 34px;
    color: var(--ink); text-transform: uppercase; letter-spacing: 1px;
  }
  .share-note {
    position: absolute; right: 64px; top: 1120px;
    display: flex; align-items: center; gap: 10px;
    font-weight: 900; font-style: italic; font-size: 32px;
    color: var(--ink); text-transform: uppercase; white-space: nowrap;
  }
  .share-icon { width: 34px; height: 38px; }
</style>
</head>
<body>
  <header>
    <div class="headline-bar"></div>
    <span class="headline-text headline-lead">FIND THE</span>
    <h1 class="headline-highlight">BEST DEAL</h1>
    <span class="headline-text headline-tail">WITH LOCAL:</span>
  </header>

  <div class="vehicle-photo" role="img" aria-label="Orange three-door hatchback with tinted rear windows, black roof and white alloy wheels"></div>

  <svg class="connectors" viewBox="0 0 1200 1200" aria-hidden="true">
    <defs>
      <marker id="arrowhead" viewBox="0 0 10 10" refX="9" refY="5" markerWidth="7" markerHeight="7" orient="auto">
        <path d="M0 0 L10 5 L0 10 Z" fill="#5cad34"/>
      </marker>
    </defs>
    <g fill="none" stroke="#8a8a8a" stroke-width="3" marker-end="url(#arrowhead)">
      <polyline points="128,326 108,346 108,458 226,458"/>
      <polyline points="820,300 700,300 640,380"/>
      <polyline points="128,830 128,760 186,650"/>
      <polyline points="1040,780 1040,630 1030,585"/>
    </g>
  </svg>

  <p class="callout callout-tint">Window<br>Tinters</p>
  <p class="callout callout-roof">Roof Vinyl<br>Wrappers</p>
  <p class="callout callout-wheels">Alloy Wheel<br>Refurbishers</p>
  <p class="callout callout-ecu">ECU<br>Remappers</p>

  <div class="cta-button">Search for free!</div>
  <svg class="cta-pointer" viewBox="0 0 56 46" aria-hidden="true">
    <path d="M0 0 L28 46 L56 0 L28 14 Z" fill="#2b2b2b"/>
  </svg>

  <footer>
    <div class="brand-name">Tunematch</div>
    <div class="share-note">
      <svg class="share-icon" viewBox="0 0 34 38" aria-hidden="true">
        <g fill="#f28c1c" stroke="#f28c1c" stroke-width="3">
          <line x1="8" y1="19" x2="26" y2="8"/>
          <line x1="8" y1="19" x2="26" y2="30"/>
          <circle cx="7" cy="19" r="6"/>
          <circle cx="27" cy="7" r="6"/>
          <circle cx="27" cy="31" r="6"/>
        </g>
      </svg>
      <span>Please share me!</span>
    </div>
  </footer>
</body>
</html>
```